DORVI
Stationery
Project: DORVI
DORVI -
Creative Brief
Professional
Tobias Wrenfeld
DORVI FZ LLC PO Box 58716 Ras al Khaimah, UAE
Africa: (+256) 701.558.946
North America: (+1) 416.987.6012
tobias.wrenfeld@dorvicorp-example.com
Please use the red and black theme.

```html
<!DOCTYPE html>
<html lang="en">
<head>
<meta charset="utf-8">
<title>DORVI Stationery Concept</title>
<link rel="stylesheet" href="https://fonts.googleapis.com/css2?family=Arimo:wght@400;700&display=swap">
<style>
  :root {
    --board-dark: #141414;
    --board-mid: #262626;
    --paper: #ffffff;
    --ink: #1c1c1c;
    --grey-text: #6f6f6f;
    --brand-red: #c8202a;
    --band-dark: #2b2b2b;
    --label: #f2f2f2;
  }
  * { margin: 0; padding: 0; box-sizing: border-box; }
  html, body { width: 1200px; height: 530px; overflow: hidden; }
  body {
    font-family: "Arimo", Arial, sans-serif;
    background:
      repeating-linear-gradient(90deg, rgba(255,255,255,0.025) 0 3px, rgba(0,0,0,0) 3px 9px),
      radial-gradient(ellipse at 50% 40%, var(--board-mid), var(--board-dark) 75%);
    color: var(--label);
    position: relative;
  }
  .board-title { position: absolute; left: 30px; top: 26px; font-size: 21px; font-weight: 700; }
  .section-label { position: absolute; font-size: 16px; color: var(--label); white-space: nowrap; }
  .section-label.small { font-size: 13px; }

  .mark { display: inline-flex; align-items: center; gap: 6px; white-space: nowrap; }
  .mark-dot { border-radius: 50%; background: var(--brand-red); flex: none; }
  .mark-name { font-weight: 700; color: var(--ink); letter-spacing: 0.5px; }

  .contact, .card-details { white-space: nowrap; }

  .hero-mark { position: absolute; left: 36px; top: 94px; }
  .hero-mark .mark-dot { width: 42px; height: 42px; }
  .hero-mark .mark-name { color: #4a4a4a; font-size: 18px; display: block; }
  .hero-mark .tagline { color: #4a4a4a; font-size: 9px; display: block; }

  .sheet { position: absolute; background: var(--paper); }

  .card-front { left: 36px; top: 211px; width: 156px; height: 80px; }
  .card-front .mark { position: absolute; left: 8px; top: 31px; gap: 5px; }
  .card-front .mark-dot { width: 16px; height: 16px; }
  .card-front .mark-name { font-size: 13px; }
  .card-details { position: absolute; left: 82px; top: 22px; font-size: 4px; line-height: 5.6px; color: var(--grey-text); }
  .card-details .person { color: var(--brand-red); font-weight: 700; }

  .card-plain { left: 36px; top: 299px; width: 156px; height: 78px; }
  .card-back { left: 36px; top: 391px; width: 156px; height: 82px; }
  .card-back .mark-dot { position: absolute; left: 66px; top: 29px; width: 24px; height: 24px; }

  .letterhead { top: 82px; width: 305px; height: 408px; }
  .letterhead.one { left: 252px; }
  .letterhead.two { left: 576px; }
  .letterhead .mark { position: absolute; left: 22px; top: 19px; }
  .letterhead .mark-dot { width: 24px; height: 24px; }
  .letterhead .mark-name { font-size: 19px; }
  .letterhead .contact { position: absolute; left: 148px; top: 20px; font-size: 4.5px; line-height: 6px; color: var(--grey-text); }

  .envelope-flap { left: 910px; top: 84px; width: 254px; height: 146px; overflow: hidden; }
  .envelope-flap svg { position: absolute; left: 0; top: 0; }
  .flap-dot { position: absolute; left: 118px; top: 78px; width: 18px; height: 18px; border-radius: 50%; background: var(--brand-red); }

  .envelope-front { left: 910px; top: 238px; width: 254px; height: 115px; }
  .envelope-front .mark { position: absolute; left: 16px; top: 45px; }
  .envelope-front .mark-dot { width: 20px; height: 20px; }
  .envelope-front .mark-name { font-size: 16px; }
  .envelope-front .contact { position: absolute; left: 118px; top: 46px; font-size: 4.5px; line-height: 6px; color: var(--grey-text); }

  .envelope-back { left: 910px; top: 362px; width: 254px; height: 128px; }
  .envelope-back .mark-dot { position: absolute; left: 20px; top: 58px; width: 12px; height: 12px; }
  .envelope-back .contact { position: absolute; left: 44px; top: 58px; font-size: 4.5px; line-height: 6px; color: var(--grey-text); }
</style>
</head>
<body>
  <h1 class="board-title">Stationary Concept</h1>

  <div class="hero-mark mark">
    <span class="mark-dot"></span>
    <span><span class="mark-name">DORVI</span><span class="tagline">Strategic Corporate Services</span></span>
  </div>

  <p class="section-label" style="left:36px; top:172px;">Bussiness Card Front</p>

  <div class="sheet card-front">
    <div class="mark"><span class="mark-dot"></span><span class="mark-name">DORVI</span></div>
    <div class="card-details">
      <div class="person">Tobias Wrenfeld</div>
      <div>DORVI FZ LLC</div>
      <div>PO Box 58716</div>
      <div>Ras al Khaimah, UAE</div>
      <div>Africa: (+256) 701.558.946</div>
      <div>N. America: (+1) 416.987.6012</div>
    </div>
  </div>
  <div class="sheet card-plain"></div>
  <div class="sheet card-back"><span class="mark-dot"></span></div>

  <p class="section-label" style="left:36px; top:484px;">Bussiness Card Back</p>

  <p class="section-label small" style="left:538px; top:48px;">Letter Head Concept</p>

  <div class="sheet letterhead one">
    <div class="mark"><span class="mark-dot"></span><span class="mark-name">DORVI</span></div>
    <div class="contact">
      <div>DORVI FZ LLC PO Box 58716</div>
      <div>Ras al Khaimah, UAE</div>
      <div>Africa: (+256) 701.558.946</div>
      <div>North America: (+1) 416.987.6012</div>
    </div>
  </div>

  <div class="sheet letterhead two">
    <div class="mark"><span class="mark-dot"></span><span class="mark-name">DORVI</span></div>
    <div class="contact">
      <div>DORVI FZ LLC PO Box 58716</div>
      <div>Ras al Khaimah, UAE</div>
      <div>Africa: (+256) 701.558.946</div>
      <div>tobias.wrenfeld@dorvicorp-example.com</div>
    </div>
  </div>

  <p class="section-label small" style="left:985px; top:58px;">Envoulpe Concept</p>

  <div class="sheet envelope-flap">
    <svg width="254" height="146" viewBox="0 0 254 146" aria-hidden="true">
      <polyline points="0,4 127,58 254,4" fill="none" stroke="#d5d5d5" stroke-width="1"/>
      <path d="M0,70 H254 V104 H0 Z" fill="var(--band-dark)"/>
      <polyline points="0,138 127,116 254,138" fill="none" stroke="#d5d5d5" stroke-width="1"/>
    </svg>
    <span class="flap-dot"></span>
  </div>

  <div class="sheet envelope-front">
    <div class="mark"><span class="mark-dot"></span><span class="mark-name">DORVI</span></div>
    <div class="contact">
      <div>DORVI FZ LLC PO Box 58716</div>
      <div>Ras al Khaimah, UAE</div>
      <div>Africa: (+256) 701.558.946</div>
      <div>North America: (+1) 416.987.6012</div>
    </div>
  </div>

  <div class="sheet envelope-back">
    <span class="mark-dot"></span>
    <div class="contact">
      <div>DORVI FZ LLC</div>
      <div>PO Box 58716, Ras al Khaimah, UAE</div>
    </div>
  </div>
</body>
</html>
```